Tinker's Fox sports bar beer & food menu

We need a menu design for our gastropub sports bar in L.A.'s Sawtelle Neighborhood (Little Osaka). We have a full-bar (hard liquor, craft beer, wine and cocktails) . We have a lunch and dinner menu as well as a happy hour menu. On Sundays we have a seperate menu with brunch items. The design concept is a British pub type of sports bar. We're looking for something different from our existing menu design. Ideally something cleaner and more legible. It should mesh a simple, modern sensibility with the more traditional darkened pub style of our interior design.

You can check out our Venuvista page for photos of the interior/exterior:
https://www.venuvista.com/biz_photos/tinkers-fox-los-angeles?tab=interior

You can view our existing menu here:
https://www.venuvista.com/biz_photos/tinkers-fox-los-angeles?tab=menu

If there's an area of the design that can be a little more playful it's our highlighted event schedule so that the events will stand out.

Target Market(s)

Age of 25 and up. Sawtelle is a cultural hub that caters to a younger, moderately affluent crowd.

Industry/Entity Type

Sports Bar

Font styles to use
Sans Serif

Colors

Designer to choose colors to be used in the design.

Requirements
Must have
• Logo, highlighted event schedule (beer pong Monday, trivia Tuesday, taco Tuesday, whiskey Wednesday, karaoke Saturday). The menu should be easy to read in a darkened bar. We'll be printing on standard 8.5x11 in portrait.
Nice to have
• We're trying to have the menu take up as few pages as possible.
Should not have
• We're trying to have the menu take up as few pages as possible. Food photography isn't necessary. A cover isn't necessary. Please avoid clip art of food.

```html
<!DOCTYPE html>
<html lang="en">
<head>
<meta charset="utf-8">
<title>Tinker's Fox – Happy Hour Menu</title>
<link rel="stylesheet" href="https://fonts.googleapis.com/css2?family=Open+Sans:wght@400;600;700;800&family=Special+Elite&display=swap">
<style>
  :root {
    --backdrop: #7aa3d4;
    --menu-black: #000000;
    --panel-black: #111111;
    --accent: #fbb03b;
    --ink: #ffffff;
    --ink-soft: #e6e6e6;
    --bar-ink: #111111;
  }
  * { margin: 0; padding: 0; box-sizing: border-box; }
  html, body { width: 1200px; height: 1200px; overflow: hidden; }
  body {
    background: var(--backdrop);
    font-family: "Open Sans", Arial, sans-serif;
    color: var(--ink);
  }
  .menu {
    position: absolute;
    left: 150px; top: 20px;
    width: 900px; height: 1160px;
    background: var(--menu-black);
  }
  .menu__panel {
    position: absolute;
    left: 454px; top: 0;
    width: 411px; height: 1076px;
    background: var(--panel-black);
  }
  .brand {
    position: absolute;
    left: 0; right: 0; top: 36px;
    display: flex; flex-direction: column; align-items: center;
  }
  .brand__name {
    display: flex; align-items: center; gap: 10px;
    font-weight: 600;
    font-size: 30px;
    letter-spacing: 1px;
    line-height: 1;
  }
  .brand__dot { width: 14px; height: 14px; border-radius: 50%; background: var(--ink); }
  .brand__tagline { margin-top: 6px; margin-left: 24px; font-size: 8px; letter-spacing: 4px; }
  .title {
    position: absolute;
    left: 0; right: 0; top: 124px;
    text-align: center;
    font-family: "Special Elite", "Courier New", monospace;
    font-size: 86px;
    line-height: 1;
    letter-spacing: 2px;
    word-spacing: -10px;
  }
  .title__warm { color: var(--accent); }
  .title__cool { color: var(--ink); }
  .section-bar {
    position: absolute;
    height: 29px;
    background: var(--accent);
    color: var(--bar-ink);
    font-weight: 700;
    font-size: 19px;
    letter-spacing: 1px;
    line-height: 29px;
    padding-left: 6px;
  }
  .section-bar--daily { left: 68px; top: 252px; width: 333px; }
  .section-bar--flatbreads { left: 492px; top: 597px; width: 333px; }
  .item { position: absolute; width: 340px; }
  .item--left { left: 67px; }
  .item--right { left: 491px; }
  .item__name { font-size: 14px; letter-spacing: 1.6px; text-transform: uppercase; line-height: 20px; }
  .item__price {
    position: absolute; top: 0; left: 316px;
    font-size: 14px; font-weight: 600; letter-spacing: 1.5px; line-height: 20px;
  }
  .item__price--low { top: 9px; }
  .item__desc {
    margin-top: 4px; width: 265px;
    font-size: 11.6px; line-height: 14px; letter-spacing: 0.3px;
    color: var(--ink-soft);
  }
  .events {
    position: absolute;
    left: 68px; top: 1092px;
    width: 764px; height: 48px;
    display: flex; align-items: stretch;
    border: 2px solid var(--accent);
  }
  .events__label {
    background: var(--accent);
    color: var(--bar-ink);
    font-weight: 800;
    font-size: 14px;
    letter-spacing: 1px;
    line-height: 15px;
    padding: 7px 12px 0;
    width: 110px;
  }
  .event {
    flex: 1;
    display: flex; flex-direction: column; justify-content: center; align-items: center;
    border-left: 1px dashed rgba(251,176,59,0.6);
  }
  .event:first-of-type { border-left: none; }
  .event__day { font-size: 10px; font-weight: 700; letter-spacing: 2px; color: var(--accent); line-height: 13px; }
  .event__name { font-size: 13px; font-weight: 600; letter-spacing: 1px; text-transform: uppercase; line-height: 17px; }
</style>
</head>
<body>
<main class="menu">
  <div class="menu__panel"></div>

  <header class="brand">
    <div class="brand__name"><span class="brand__dot"></span>Tinker's Fox</div>
    <div class="brand__tagline">PUB &amp; RESTAURANT</div>
  </header>

  <h1 class="title"><span class="title__warm">HAPPY</span> <span class="title__cool">HOUR</span></h1>

  <div class="section-bar section-bar--daily">HAPPY HOUR: 3-7PM DAILY</div>

  <div class="item item--left" style="top:305px"><div class="item__name">Shisito Pepper</div><div class="item__price">$6</div><div class="item__desc">Ginger Soy Sauce</div></div>
  <div class="item item--left" style="top:366px"><div class="item__name">3 Jumbo Wings</div><div class="item__price">$6</div><div class="item__desc">Sautéed with Chorizo, Roasted Almonds and Golden Raisins</div></div>
  <div class="item item--left" style="top:440px"><div class="item__name">Meatballs</div><div class="item__price">$5</div><div class="item__desc">House Marinara Sauce</div></div>
  <div class="item item--left" style="top:500px"><div class="item__name">Fried Calamari</div><div class="item__price">$6</div><div class="item__desc">Marinara Sauce</div></div>
  <div class="item item--left" style="top:561px"><div class="item__name">Tinker's Fox Nachos</div><div class="item__price">$7</div><div class="item__desc">Medley of Black Beans, Pico De Gallo, Cheese, Jalapeno and Sour Cream</div></div>
  <div class="item item--left" style="top:631px"><div class="item__name">Pan Roasted Brussel Sprouts</div><div class="item__price">$7</div><div class="item__desc" style="width:290px">Chorizo, Roasted Almonds and Golden Raisins</div></div>
  <div class="item item--left" style="top:688px"><div class="item__name">Atlantic Cod Fish N’ Chips</div><div class="item__price item__price--low">$8</div><div class="item__desc">House Tartar Sauce, Vinegar and Lemon Wedge</div></div>
  <div class="item item--left" style="top:761px"><div class="item__name">Tacos (3)</div><div class="item__price">$8</div><div class="item__desc" style="width:240px">Choose Your Protein: Chicken , Beef or Shrimp</div></div>
  <div class="item item--left" style="top:836px"><div class="item__name">Beef Sliders (3)</div><div class="item__price">$10</div><div class="item__desc" style="width:290px">Arugula, Tomato, Onion and Sharp Cheddar</div></div>
  <div class="item item--left" style="top:900px"><div class="item__name">Fried Chicken Sliders (3)</div><div class="item__price">$10</div><div class="item__desc">Coleslaw, Lime Sriracha Sauce</div></div>
  <div class="item item--left" style="top:963px"><div class="item__name">½ Dozen Oysters</div><div class="item__price item__price--low">$10</div><div class="item__desc" style="width:290px">Kelp Cove Served with Our Own Mignonette</div></div>
  <div class="item item--left" style="top:1026px"><div class="item__name">PEI Mussels</div><div class="item__price">$11</div><div class="item__desc" style="width:290px">Tequila Chipotle Sauce with Cherry Tomatoes and Cilantro</div></div>

  <div class="item item--right" style="top:254px"><div class="item__name">Charcuterie</div><div class="item__price">$13</div><div class="item__desc">Seasonal Meats and Cheese</div></div>
  <div class="item item--right" style="top:311px"><div class="item__name">Pita Bread</div><div class="item__price">$6</div><div class="item__desc">Hummus Sauce, Shredded Chicken and Avocado</div></div>
  <div class="item item--right" style="top:384px"><div class="item__name">Mushroom Tart</div><div class="item__price">$6</div><div class="item__desc" style="width:300px">Portobello Creamy Mushroom with Truffle Oil.</div></div>
  <div class="item item--right" style="top:443px"><div class="item__name">Shrimp Cocktail (6)</div><div class="item__price">$8</div><div class="item__desc">House Cocktail Sauce</div></div>
  <div class="item item--right" style="top:503px"><div class="item__name">Tomato Bruschetta</div><div class="item__price">$6</div><div class="item__desc">Sun-Dried Tomato Pesto, Fresh basil and Tomato Balsamic Glaze</div></div>

  <div class="section-bar section-bar--flatbreads">HAPPY HOUR FLATBREADS</div>

  <div class="item item--right" style="top:658px"><div class="item__name">Margherita</div><div class="item__price">$6</div><div class="item__desc">Fresh Mozzarella, Roma Tomatoes and Italian Basil</div></div>
  <div class="item item--right" style="top:730px"><div class="item__name">Vegetarian</div><div class="item__price">$7</div><div class="item__desc">Brussel Sprouts, Peppers, Onions, Zucchini, Goat Cheese , Smoked Mozzarella, Topped with a Balsamic Reduction</div></div>
  <div class="item item--right" style="top:812px"><div class="item__name">Tikka Masala</div><div class="item__price">$7</div><div class="item__desc">Tandoori Chicken, Fontina and Raita</div></div>
  <div class="item item--right" style="top:868px"><div class="item__name">The Primal Dog</div><div class="item__price">$7</div><div class="item__desc">Meatballs, Sausage, Chorizo, Mozzarella &amp; Fresn</div></div>
  <div class="item item--right" style="top:938px"><div class="item__name">Prosciutto &amp; Arugula</div><div class="item__price">$7</div><div class="item__desc">Red Onionin, Parmesans, Mozzarella</div></div>
  <div class="item item--right" style="top:996px"><div class="item__name">Chicken Tikka Masala</div><div class="item__price">$7</div><div class="item__desc">Tandoori, Chicken, Fontini and Raita</div></div>

  <section class="events" aria-label="Weekly events">
    <div class="events__label">WEEKLY<br>EVENTS</div>
    <div class="event"><span class="event__day">MONDAY</span><span class="event__name">Beer Pong</span></div>
    <div class="event"><span class="event__day">TUESDAY</span><span class="event__name">Trivia</span></div>
    <div class="event"><span class="event__day">TUESDAY</span><span class="event__name">Tacos</span></div>
    <div class="event"><span class="event__day">WEDNESDAY</span><span class="event__name">Whiskey</span></div>
    <div class="event"><span class="event__day">SATURDAY</span><span class="event__name">Karaoke</span></div>
  </section>
</main>
</body>
</html>
```